BRELM - Letterhead

Willowmere Institute of Letters and Crafts (BRELM) is a non-profit organization that operates two tuition-free public schools - BRELM Elementary for grades K to 5th and BRELM College Prep for grades 6-12.

We are looking for a letterhead primarily to be used on Google Docs and Microsoft Word. Attached are two versions of our logo. One with our name spelled out and one with the acronym.

For Letterhead, we would like 3 addresses listed:

BRELM HQ
41872 Hollow Brook Lane, Suite 308
Laguna Niguel, CA 92677

BRELM Elementary (K-5)
18460 Marsh Ridge Boulevard
Laguna Niguel, CA 92677

BRELM College Prep (6-12)
27314 Del Sol Terrace
San Juan Capistrano, CA 92675

Our Phone Number is (555) 418-7062
Our Fax Number is the same (555) 418-7062

Our website is www.brelmschools.org

Target Market(s)

Education

Industry/Entity Type

Education

Font styles to use
Sans Serif

Colors
0054AA
0677BA
7BADD7
CADEEF
E8F1F8

Requirements
Must have
• Logo, Address, Phone Number, Website.
Nice to have
• Modern and clean design.
Should not have
• Prefer that there is no bleed -- the letterhead will mostly be used in PDF format however sometimes it will be printed and our printers can not do a full bleed

```html
<!DOCTYPE html>
<html lang="en">
<head>
<meta charset="utf-8">
<title>BRELM Letterhead</title>
<link href="https://fonts.googleapis.com/css2?family=Quicksand:wght@500;600&display=swap" rel="stylesheet">
<style>
  :root {
    --backdrop: #d4d4d4;
    --paper: #ffffff;
    --ink: #1d3c9d;
    --rule: #1b7fc8;
    --band-light: #1b8ad0;
    --band-dark: #1b46a0;
  }
  * { margin: 0; padding: 0; box-sizing: border-box; }
  html, body {
    width: 1200px; height: 1200px; overflow: hidden;
    background: var(--backdrop);
    font-family: "Quicksand", sans-serif;
    color: var(--ink);
  }
  .letterhead {
    position: absolute; left: 160px; top: 30px;
    width: 882px; height: 1140px;
    background: var(--paper);
  }
  .brand-name {
    position: absolute; left: 16px; top: 70px;
    font-size: 26px; font-weight: 600; letter-spacing: 0.5px;
    line-height: 30px;
  }
  .address {
    position: absolute; top: 31px;
    font-size: 13px; font-weight: 500; font-style: normal;
    line-height: 17.5px; letter-spacing: 0.2px; white-space: nowrap;
  }
  .address--hq { left: 172px; }
  .address--elementary { left: 428px; }
  .address--prep { left: 657px; }
  .divider {
    position: absolute; top: 31px; width: 1.5px; height: 56px;
    background: var(--rule);
  }
  .divider--one { left: 414px; }
  .divider--two { left: 643px; }
  .header-rule {
    position: absolute; left: 0; top: 109px; width: 100%; height: 1.5px;
    background: var(--rule);
  }
  .contact {
    position: absolute; top: 1088px;
    display: flex; align-items: center; gap: 10px;
    font-size: 14px; font-weight: 500; letter-spacing: 0.4px;
    white-space: nowrap;
  }
  .contact svg { width: 18px; height: 20px; fill: none; stroke: var(--rule); stroke-width: 1.6; }
  .contact--phone { left: 72px; }
  .contact--fax { left: 386px; }
  .contact--web { left: 672px; }
  .band-light {
    position: absolute; left: 0; top: 1116px; width: 100%; height: 5px;
    background: var(--band-light);
  }
  .band-dark {
    position: absolute; left: 0; top: 1121px; width: 100%; height: 19px;
    background: var(--band-dark);
  }
</style>
</head>
<body>
  <main class="letterhead">
    <div class="brand-name">BRELM</div>

    <address class="address address--hq">BRELM HQ<br>41872 Hollow Brook Lane, Suite 308<br>Laguna Niguel, CA 92677</address>
    <span class="divider divider--one"></span>
    <address class="address address--elementary">BRELM Elementary (K-5)<br>18460 Marsh Ridge Boulevard<br>Laguna Niguel, CA 92677</address>
    <span class="divider divider--two"></span>
    <address class="address address--prep">BRELM College Prep (6-12)<br>27314 Del Sol Terrace<br>San Juan Capistrano, CA 92675</address>

    <div class="header-rule"></div>

    <div class="contact contact--phone">
      <svg viewBox="0 0 18 20" aria-hidden="true"><path d="M4 2 L7 2 L8 6 L6 8 Q7 12 11 14 L13 12 L16 13 L16 16 Q14 19 10 17 Q3 13 2 6 Q2 3 4 2 Z" fill="var(--rule)" stroke="none"/></svg>
      <span>(555) 418-7062</span>
    </div>
    <div class="contact contact--fax">
      <svg viewBox="0 0 18 20" aria-hidden="true"><rect x="2" y="7" width="15" height="11" rx="1"/><rect x="5" y="2" width="8" height="6"/><path d="M9 11h5M9 14h5M5 10v6"/></svg>
      <span>(555) 418-7062</span>
    </div>
    <div class="contact contact--web">
      <svg viewBox="0 0 18 20" aria-hidden="true"><circle cx="9" cy="10" r="7"/><ellipse cx="9" cy="10" rx="3" ry="7"/><path d="M2 10h14M3 6.5h12M3 13.5h12"/></svg>
      <span>www.brelmschools.org</span>
    </div>

    <div class="band-light"></div>
    <div class="band-dark"></div>
  </main>
</body>
</html>
```